Business Card design for Founder and CEO of new shoe company

I am looking for a business card design for my new shoe company called Strapwell.

I am launching the company this April. Strapwell shoes offers slip-on athletic and casual style shoes for men and women. The unique selling point of the brand is that all of our shoe exist without shoelaces. I have included a link to the website to offer additional information about the company, see product images, and gain inspiration for the design. You can use the store owner password "Strapwell" to access the website.

www.Strapwell.example

Thanks,
Dan Hollis

Target Market(s)

Active Men and Women ages 16-45

Industry/Entity Type

Business

Contact Information for Business Card

Dan Hollis
Founder and CEO
www.Strapwell.example
danhollis@Strapwell.example
888-555-0187 / 888-5STRAPW
Strapwell, LLC
2284 N Tamsin Ave
Chicago, IL 60699

Requirements
Must have
• Be able to quickly and easily tell that Strapwell is a shoe company from the business card

```html
<!DOCTYPE html>
<html lang="en">
<head>
<meta charset="utf-8">
<title>Strapwell Business Card</title>
<link href="https://fonts.googleapis.com/css2?family=Montserrat:wght@300;400;600;700&display=swap" rel="stylesheet">
<style>
  :root {
    --backdrop: #6f6f6d;
    --ink-black: #111111;
    --charcoal: #4a4a4a;
    --band-gray: #6b6b6b;
    --paper: #f4f4f4;
    --text-light: #ffffff;
    --text-muted: #bdbdbd;
    --text-dark: #2a2a2a;
    --shoe-blue: #3aa3de;
    --floor-dark: #3b3b3d;
    --wall-light: #d9d9d9;
  }
  * { margin: 0; padding: 0; box-sizing: border-box; }
  html, body { width: 1200px; height: 856px; overflow: hidden; }
  body {
    background: var(--backdrop);
    font-family: "Montserrat", Arial, sans-serif;
    position: relative;
  }
  .card {
    position: absolute;
    left: 285px;
    width: 630px;
    height: 360px;
    border-radius: 26px;
    overflow: hidden;
    box-shadow: 0 10px 30px rgba(0,0,0,0.35);
  }
  /* Back side */
  .card-back { top: 40px; background: var(--charcoal); }
  .card-back .brand-band {
    position: absolute; left: 0; right: 0; top: 92px; height: 176px;
    background: var(--paper);
    display: flex; align-items: center; justify-content: center;
  }
  .card-back .brand-name {
    font-size: 46px; font-weight: 400; color: var(--ink-black); letter-spacing: 1px;
  }
  /* Front side */
  .card-front { top: 448px; background: var(--paper); }
  .identity-panel {
    position: absolute; left: 0; top: 0; bottom: 0; width: 340px;
    background: var(--ink-black);
    padding: 118px 0 0 40px;
  }
  .person-name {
    color: var(--text-light); font-size: 28px; font-weight: 700; letter-spacing: 1.5px;
  }
  .person-title {
    color: var(--text-muted); font-size: 13px; font-weight: 300; letter-spacing: 1.5px; margin-top: 2px;
  }
  .contact-list { list-style: none; margin-top: 26px; }
  .contact-item {
    display: flex; align-items: center; gap: 10px;
    color: var(--text-light); font-size: 11px; font-weight: 400; margin-bottom: 14px;
  }
  .contact-icon { width: 18px; height: 18px; flex: none; }
  .showcase {
    position: absolute; left: 340px; top: 0; right: 0; bottom: 0;
  }
  .web-address {
    height: 48px; display: flex; align-items: flex-end; justify-content: center;
    padding-bottom: 4px; font-size: 13px; color: var(--text-dark);
  }
  .brand-strip {
    height: 44px; background: var(--band-gray);
    display: flex; align-items: center; justify-content: center;
  }
  .brand-strip .brand-name { color: var(--text-light); font-size: 24px; font-weight: 400; letter-spacing: 0.5px; }
  .street-address {
    height: 26px; display: flex; align-items: center; justify-content: center;
    font-size: 9.5px; color: var(--text-dark);
  }
  .product-photo {
    position: absolute; left: 0; right: 0; top: 118px; bottom: 0;
    background:
      radial-gradient(ellipse 60% 35% at 50% 55%, var(--shoe-blue) 0%, rgba(58,163,222,0.6) 55%, rgba(58,163,222,0) 100%),
      linear-gradient(180deg, var(--wall-light) 0%, var(--wall-light) 45%, var(--floor-dark) 75%, var(--floor-dark) 100%);
  }
</style>
</head>
<body>

  <section class="card card-back" aria-label="Card back">
    <div class="brand-band">
      <span class="brand-name">Strapwell</span>
    </div>
  </section>

  <section class="card card-front" aria-label="Card front">
    <div class="identity-panel">
      <h1 class="person-name">DAN HOLLIS</h1>
      <p class="person-title">FOUNDER AND CEO</p>
      <ul class="contact-list">
        <li class="contact-item">
          <svg class="contact-icon" viewBox="0 0 18 18" aria-hidden="true">
            <circle cx="9" cy="9" r="8" fill="none" stroke="#fff" stroke-width="1"/>
            <path d="M6.2 5.2l1.4-.4 1 2-.9.8a5 5 0 0 0 2.2 2.2l.8-.9 2 1-.4 1.4c-3.1.4-6.5-3-6.1-6.1z" fill="#fff"/>
          </svg>
          <span>888-555-0187 &nbsp;/&nbsp; 888-5STRAPW</span>
        </li>
        <li class="contact-item">
          <svg class="contact-icon" viewBox="0 0 18 18" aria-hidden="true">
            <circle cx="9" cy="9" r="8" fill="none" stroke="#fff" stroke-width="1"/>
            <rect x="5" y="6.2" width="8" height="5.6" fill="none" stroke="#fff" stroke-width="1"/>
            <path d="M5 6.4l4 3 4-3" fill="none" stroke="#fff" stroke-width="1"/>
          </svg>
          <span>danhollis@Strapwell.example</span>
        </li>
      </ul>
    </div>

    <div class="showcase">
      <p class="web-address">www.Strapwell.example</p>
      <div class="brand-strip"><span class="brand-name">Strapwell</span></div>
      <p class="street-address">2284 N Tamsin Ave Chicago, IL 60699</p>
      <div class="product-photo" role="img" aria-label="Photo of a pair of blue slip-on athletic shoes on a dark floor"></div>
    </div>
  </section>

</body>
</html>
```